Kick The Pickle! Summer One Act Festival

I need a poster design for a summer festival of short comedy plays in San Francisco, all with a historical or intellectual theme! From Ancient Greece to the Russian Revolution to Cold War Politics to College Admissions! The target audience demographic is 20-30 year old San Francisco "hipster types" who will be attending a food truck festival. The festival performance dates are Friday evenings, July 22 to August 15! We would like a clever, antique looking design that conveys comedy and history. We would also like the names of the plays, all by the same author, Milo Tennant, on the poster as well! The titles are:

Tentaxi
Wine Without Dread
That Huge Dumb Gothic Epic
Tune Tickle
Freshman Fumbles
Somebody Wore a Hat

Festival

```html
<!DOCTYPE html>
<html lang="en">
<head>
<meta charset="utf-8">
<title>Kick The Pickle! Summer One Act Festival</title>
<link href="https://fonts.googleapis.com/css2?family=IM+Fell+English+SC&family=Questrial&family=Playfair+Display+SC:wght@700&family=Oswald:wght@400;600&family=Lobster&family=Cinzel:wght@400&family=Russo+One&family=Rye&family=Poiret+One&family=Graduate&family=Pacifico&display=swap" rel="stylesheet">
<style>
  :root {
    --ink: #141414;
    --paper-top: #6c7a66;
    --paper-glow: #e9ecb0;
    --paper-mid: #d7d38e;
    --paper-bottom: #b07f52;
    --white: #fbfaf2;
    --tag-ink: #2c2a1c;
    --rule: rgba(40, 40, 30, 0.45);
    --wine-red: #d42a35;
    --gold: #c9a43a;
    --gold-dark: #7d6214;
    --maroon: #7b1b2e;
    --tickle-red: #d9403e;
    --hat-yellow: #f0c94a;
    --fumble-red: #c8242c;
    --ornament: rgba(30, 30, 25, 0.35);
  }
  * { margin: 0; padding: 0; box-sizing: border-box; }
  html, body { width: 848px; height: 1200px; overflow: hidden; }
  body { background: var(--paper-top); }
  .poster {
    position: relative; width: 848px; height: 1200px; overflow: hidden;
    background:
      radial-gradient(ellipse 70% 38% at 50% 48%, var(--paper-glow) 0%, rgba(233,236,176,0) 100%),
      linear-gradient(180deg, var(--paper-top) 0%, #9aa27a 22%, var(--paper-mid) 48%, #d2b577 72%, var(--paper-bottom) 100%);
  }
  .frame-outer { position: absolute; left: 34px; top: 34px; width: 780px; height: 1132px; border: 4px solid var(--ink); }
  .frame-inner { position: absolute; left: 44px; top: 44px; width: 760px; height: 1112px; border: 1.5px solid var(--ink); }
  .ornament { position: absolute; width: 56px; height: 56px; background: var(--ornament); border-radius: 6px; }
  .ornament.tl { left: 52px; top: 52px; }
  .ornament.tr { right: 52px; top: 52px; }
  .ornament.bl { left: 52px; bottom: 52px; }
  .ornament.br { right: 52px; bottom: 52px; }
  .center { position: absolute; left: 0; width: 848px; text-align: center; }
  .presents { top: 62px; font: 17px "Questrial", sans-serif; color: var(--ink); }
  .festival-title { top: 84px; font: 400 84px/1 "IM Fell English SC", serif; color: var(--white); letter-spacing: 2px; }
  .byline { top: 184px; font: 33px "Questrial", sans-serif; color: var(--white); letter-spacing: 0.5px; }
  .rule { position: absolute; left: 46px; width: 756px; border-top: 1px dotted var(--rule); }
  .tagline { top: 247px; font: 700 17px/1.25 "Playfair Display SC", serif; color: var(--tag-ink); letter-spacing: 1.5px; }
  .dates { top: 316px; font: 34px/1 "Oswald", sans-serif; color: var(--ink); letter-spacing: 1.5px; }
  .dates sup { font-size: 16px; vertical-align: 14px; }
  .divider-v { position: absolute; left: 424px; top: 375px; height: 735px; border-left: 1px dotted var(--rule); }
  .cell { position: absolute; width: 378px; display: flex; flex-direction: column; align-items: center; justify-content: center; text-align: center; }
  .col-l { left: 46px; } .col-r { left: 424px; }
  .row-1 { top: 375px; height: 207px; }
  .row-2 { top: 582px; height: 264px; }
  .row-3 { top: 846px; height: 264px; }
  .wine { color: var(--wine-red); font-family: "Lobster", cursive; line-height: 0.9; }
  .wine .big { font-size: 86px; }
  .wine .small { font: 20px "Questrial", sans-serif; letter-spacing: 2px; margin: 2px 0 -4px 120px; }
  .tentaxi { font: 66px "Cinzel", serif; letter-spacing: 4px; color: var(--gold); text-shadow: 1px 2px 0 var(--gold-dark); }
  .epic { font-family: "Russo One", sans-serif; color: var(--maroon); line-height: 0.98; }
  .epic .the { font-size: 40px; }
  .epic .line { font-size: 56px; letter-spacing: 1px; }
  .tickle .tune { font: 76px/1 "Pacifico", cursive; color: var(--ink); }
  .tickle .main { font: 78px/1.1 "Rye", serif; color: var(--tickle-red); text-shadow: 3px 3px 0 #3a1414; }
  .hat { line-height: 1; }
  .hat .somebody { font: 600 32px "Oswald", sans-serif; color: var(--hat-yellow); letter-spacing: 2px; margin-left: 90px; }
  .hat .wore { font: 100px "Poiret One", cursive; color: var(--ink); }
  .hat .a-hat { font: 64px "Poiret One", cursive; color: var(--hat-yellow); }
  .hat .a-hat span { color: var(--ink); font-size: 34px; margin-right: 10px; }
  .fresh .word { font: 60px/1 "Graduate", serif; color: var(--white); text-shadow: 2px 3px 3px rgba(0,0,0,0.45); }
  .fresh .script { font: 52px/1.1 "Lobster", cursive; color: var(--fumble-red); margin-top: 14px; text-shadow: 1px 1px 0 #5a1010; }
  .venue { top: 1117px; font: 20px "Questrial", sans-serif; color: var(--white); word-spacing: 4px; }
</style>
</head>
<body>
<main class="poster">
  <div class="frame-outer"></div>
  <div class="frame-inner"></div>
  <div class="ornament tl" role="img" aria-label="Corner flourish ornament"></div>
  <div class="ornament tr" role="img" aria-label="Corner flourish ornament"></div>
  <div class="ornament bl" role="img" aria-label="Corner flourish ornament"></div>
  <div class="ornament br" role="img" aria-label="Corner flourish ornament"></div>

  <p class="center presents">Summer One Act Festival presents ...</p>
  <h1 class="center festival-title">Kick The Pickle!</h1>
  <p class="center byline">6 Original One Act Plays by Milo Tennant</p>
  <div class="rule" style="top:236px"></div>
  <p class="center tagline">From Ancient Greece to the Russian Revolution<br>to Cold War Politics to College Admissions!</p>
  <div class="rule" style="top:302px"></div>
  <p class="center dates">FRIDAY EVENINGS, JULY 22<sup>ND</sup> - AUGUST 15<sup>TH</sup></p>
  <div class="rule" style="top:375px"></div>
  <div class="rule" style="top:582px"></div>
  <div class="rule" style="top:846px"></div>
  <div class="rule" style="top:1110px"></div>
  <div class="divider-v"></div>

  <section class="cell col-l row-1 wine">
    <span class="big">Wine</span><span class="small">WITHOUT</span><span class="big">Dread</span>
  </section>
  <section class="cell col-r row-1 tentaxi">TENTAXI</section>
  <section class="cell col-l row-2 epic">
    <span class="the">THAT</span><span class="line">HUGE DUMB</span><span class="line">GOTHIC</span><span class="line">EPIC</span>
  </section>
  <section class="cell col-r row-2 tickle">
    <span class="tune">Tune</span><span class="main">TICKLE</span>
  </section>
  <section class="cell col-l row-3 hat">
    <span class="somebody">SOMEBODY</span><span class="wore">Wore</span><span class="a-hat"><span>A</span>Hat</span>
  </section>
  <section class="cell col-r row-3 fresh">
    <span class="word">FRESHMAN</span><span class="script">Fumbles</span>
  </section>

  <p class="center venue">Building F, Room 214, Harbor Hall, Port Alder, CA</p>
</main>
</body>
</html>
```